Design a product reviews website

We need a website design and simple logo for the brand Qorviln.com. The website will provide reviews of technology products and services. The brand and website should be approachable but should also be trustworthy and high quality. The deliverable should be designs, specs and assets that I can provide to a development team to build the website.

Target Market(s)

People researching products to buy.

Industry/Entity Type

Product

Logo Text

Qorviln.com

Number of Pages Required

5+ page

Font styles to use
Sans Serif

Colors
0492cd
0355a3
3176b5
33a6d7
85cae6
85abd2
cedeed
cee9f5

Requirements
Must have
• - Designs for the Homepage, Category and Article pages.
• - Designs for web and mobile.
• - Designs details for the engineering team to use for development.
• - I'm open to other colors than the preferences I chose but I'm more likely to like blues, greys and blacks.

```html
<!DOCTYPE html>
<html lang="en">
<head>
<meta charset="utf-8">
<title>Qorviln.com – Product Reviews</title>
<link href="https://fonts.googleapis.com/css2?family=Roboto:wght@300;400;500;700&display=swap" rel="stylesheet">
<style>
:root{
  --blue:#0492cd;
  --blue-dark:#0355a3;
  --blue-mid:#3176b5;
  --blue-light:#33a6d7;
  --navy:#0b3f7a;
  --ink:#2b2b2b;
  --muted:#777;
  --line:#dcdcdc;
  --page:#ececec;
  --white:#fff;
}
*{box-sizing:border-box;margin:0;padding:0}
html,body{width:1200px;height:2304px;overflow:hidden}
body{font-family:"Roboto",sans-serif;color:var(--ink);background:var(--page);position:relative}

.site-header{position:absolute;top:0;left:0;width:1200px;height:40px;background:var(--white);border-bottom:2px solid var(--blue)}
.brand{position:absolute;left:104px;top:8px;display:flex;align-items:center;gap:8px;font-weight:700;font-size:22px;color:var(--ink)}
.brand-mark{width:20px;height:20px;background:var(--blue)}
.search{position:absolute;left:620px;top:9px;width:388px;height:24px;border:1px solid var(--line);font-size:11px;color:#999;padding:5px 8px}
.search-btn{position:absolute;left:1008px;top:9px;width:60px;height:24px;background:var(--blue);display:flex;align-items:center;justify-content:center}
.menu-icon{position:absolute;left:1098px;top:12px}

.hero{position:absolute;top:40px;left:0;width:1200px;height:500px;background:linear-gradient(180deg,#3a3431 0%,#5b4f48 45%,#2a2524 100%)}
.hero h1{position:absolute;left:0;right:0;top:210px;text-align:center;color:var(--white);font-weight:400;font-size:42px;line-height:52px}

.category-nav{position:absolute;left:64px;top:588px;width:204px;background:var(--white);border:1px solid var(--line);list-style:none}
.category-nav li{height:48px;display:flex;align-items:center;gap:12px;padding-left:12px;font-size:13px;color:#555;border-bottom:1px solid #eee;text-transform:uppercase}
.category-nav li.active{background:var(--blue);color:var(--white)}
.category-nav .ico{width:22px;height:18px;background:#bbb;border-radius:2px}
.category-nav li.active .ico{background:var(--white)}

.panel{position:absolute;top:588px;background:var(--white);border:1px solid var(--line)}
.panel-title{height:52px;line-height:52px;padding-left:16px;font-size:15px;font-weight:500;color:#444;border-bottom:1px solid var(--line);text-transform:uppercase}
.new-products{left:304px;width:536px;height:1112px}
.popular{left:872px;width:260px;height:1112px}

.thumb{position:absolute}
.tag{position:absolute;bottom:8px;background:var(--blue);color:var(--white);font-size:11px;font-weight:500;padding:6px 10px;text-transform:uppercase}
.card-text{position:absolute;font-size:14px;color:#555;line-height:20px}
.author{position:absolute;display:flex;align-items:center;gap:12px;font-size:14px}
.avatar{width:34px;height:34px;background:#9aa3ad}
.author-name{color:var(--blue-mid);font-weight:500}
.posted{position:absolute;font-size:11px;color:var(--muted)}

.load-more{position:absolute;left:304px;top:1708px;width:828px;height:52px;background:#a9a9a9;color:var(--white);display:flex;align-items:center;justify-content:center;gap:10px;font-size:14px}

.about{position:absolute;left:0;top:1808px;width:1200px;height:452px;background:linear-gradient(180deg,var(--blue-mid),var(--blue-dark))}
.about h2{position:absolute;left:0;right:0;top:84px;text-align:center;color:var(--white);font-weight:300;font-size:42px;letter-spacing:1px}
.about p{position:absolute;left:190px;width:820px;top:167px;text-align:center;color:var(--white);font-size:14px;line-height:24px}

.site-footer{position:absolute;left:0;top:2260px;width:1200px;height:44px;background:var(--navy);color:#dfe9f5;font-size:12px;text-align:center;line-height:44px}
</style>
</head>
<body>

<header class="site-header">
  <div class="brand"><span class="brand-mark"></span>Qorviln.com</div>
  <div class="search">Search</div>
  <div class="search-btn">
    <svg width="14" height="14" viewBox="0 0 14 14"><circle cx="6" cy="6" r="4.5" fill="none" stroke="#fff" stroke-width="2"/><line x1="9.5" y1="9.5" x2="13" y2="13" stroke="#fff" stroke-width="2"/></svg>
  </div>
  <svg class="menu-icon" width="20" height="16" viewBox="0 0 20 16"><g fill="#333"><rect x="0" y="1" width="3" height="3"/><rect x="5" y="1" width="15" height="3"/><rect x="0" y="7" width="3" height="3"/><rect x="5" y="7" width="15" height="3"/><rect x="0" y="13" width="3" height="3"/><rect x="5" y="13" width="15" height="3"/></g></svg>
</header>

<section class="hero" role="img" aria-label="Dark photo of a smartwatch and a fitness band on a table">
  <h1>The Best Product And Services Reviews<br>And Rankings</h1>
</section>

<ul class="category-nav">
  <li class="active"><span class="ico"></span>Home</li>
  <li><span class="ico"></span>Appliances</li>
  <li><span class="ico"></span>Computers</li>
  <li><span class="ico"></span>Electronics</li>
  <li><span class="ico"></span>Home Security</li>
  <li><span class="ico"></span>Mobiles</li>
  <li><span class="ico"></span>Smart Home</li>
  <li><span class="ico"></span>Software</li>
</ul>

<section class="panel new-products">
  <div class="panel-title">New Products</div>

  <div class="thumb" style="left:16px;top:60px;width:504px;height:240px;background:linear-gradient(135deg,#5b3a2c,#a07a5e)" role="img" aria-label="Living room with a TV and speakers">
    <span class="tag" style="right:86px">Home</span><span class="tag" style="right:8px">Speaker</span>
  </div>
  <div class="card-text" style="left:16px;top:312px">Lorem ipsum Dolor Sit Amet</div>
  <div class="author" style="left:16px;top:350px"><span class="avatar"></span><span class="author-name">Mark Dalen</span></div>
  <div class="posted" style="right:16px;top:362px">Posted On 11 Aug, 2016</div>

  <div class="thumb" style="left:16px;top:420px;width:244px;height:200px;background:linear-gradient(135deg,#cfd6dc,#8fa3b4)" role="img" aria-label="Hand using a smart home wall panel">
    <span class="tag" style="right:8px">Home</span>
  </div>
  <div class="card-text" style="left:16px;top:628px;width:244px">Lorem ipsum dolor sit amet, consectetuer elit</div>
  <div class="thumb" style="left:276px;top:420px;width:244px;height:200px;background:linear-gradient(135deg,#e9e6e2,#b8b2aa)" role="img" aria-label="Two smartphones side by side">
    <span class="tag" style="right:8px">Home</span>
  </div>
  <div class="card-text" style="left:276px;top:628px;width:244px">Lorem ipsum dolor sit amet, consectetuer elit</div>

  <div class="thumb" style="left:16px;top:732px;width:504px;height:240px;background:linear-gradient(135deg,#8a4a32,#2c2624)" role="img" aria-label="Black audio speaker against a brick wall">
    <span class="tag" style="right:8px">Budget</span>
  </div>
  <div class="card-text" style="left:16px;top:984px">Lorem ipsum Dolor Sit Amet</div>
  <div class="author" style="left:16px;top:1022px"><span class="avatar"></span><span class="author-name">Mark Dalen</span></div>
  <div class="posted" style="right:16px;top:1034px">Posted On 11 Aug, 2016</div>
</section>

<section class="panel popular">
  <div class="panel-title">Popular Products</div>
  <div class="thumb" style="left:12px;top:60px;width:234px;height:172px;background:linear-gradient(135deg,#7a4b2e,#c99367)" role="img" aria-label="Kitchen appliances on a counter"><span class="tag" style="right:8px">Home</span></div>
  <div class="card-text" style="left:12px;top:240px;width:234px">Lorem ipsum dolor sit amet, consectetuer</div>
  <div class="thumb" style="left:12px;top:324px;width:234px;height:172px;background:linear-gradient(135deg,#6d6a66,#b4aca2)" role="img" aria-label="Modern kitchen interior"><span class="tag" style="right:8px">Home</span></div>
  <div class="card-text" style="left:12px;top:504px;width:234px">Lorem ipsum dolor sit amet, consectetuer</div>
  <div class="thumb" style="left:12px;top:588px;width:234px;height:172px;background:linear-gradient(135deg,#2f5e8f,#8fb4d4)" role="img" aria-label="Laptop on a desk"><span class="tag" style="right:8px">Home</span></div>
  <div class="card-text" style="left:12px;top:768px;width:234px">Lorem ipsum dolor sit amet, consectetuer</div>
  <div class="thumb" style="left:12px;top:852px;width:234px;height:172px;background:linear-gradient(135deg,#3c4a5c,#8e9bab)" role="img" aria-label="Smart door lock on a door"><span class="tag" style="right:8px">Home</span></div>
  <div class="card-text" style="left:12px;top:1032px;width:234px">Lorem ipsum dolor sit amet, consectetuer</div>
</section>

<div class="load-more">
  <svg width="20" height="20" viewBox="0 0 20 20"><circle cx="10" cy="10" r="7" fill="none" stroke="#fff" stroke-width="2" stroke-dasharray="30 14"/></svg>
  Load More
</div>

<section class="about" role="img" aria-label="Blue-tinted photo of assorted home appliances">
  <h2>ABOUT QORVILN</h2>
  <p>Lorem ipsum dolor sit amet, consectetuer adipiscing elit, sed diam nonummy nibh euismod tincidunt ut laoreet dolore magna aliquam erat volutpat. Ut wisi enim ad minim veniam, quis nostrud exerci tation ullamcorper suscipit lobortis nisl ut aliquip ex ea commodo consequat. Duis autem vel eum iriure dolor in hendrerit in vulputate velit esse molestie consequat, vel illum dolore eu feugiat nulla facilisis at vero eros et accumsan et iusto odio dignissim qui blandit praesent luptatum zzril delenit augue duis dolore te feugait nulla facilisi.</p>
</section>

<footer class="site-footer">Copyright © 2016 - Qorviln.com | All Rights Reserved</footer>

</body>
</html>
```